Aggressive Appliance retailer requires a Large Billboard design.

We require a large Tall billboard design it stands 4500mm high x 2400mm across. We have our own range of imported appliances called Veltrono and we provide a 5 year warranty, key pionts low price + long solid warranty. Provided are 3 products 1 x clothes washer 8 kg $699 1 x dishwasher $499 1 x side by side fridge freezer $1299 all with 5 year warranty. Company colors very bright green. Provided warranty logo / images / and an add that has the font we have preference too. I am not rigid to the above requirements and open to designers own ideas :-) I have supplied a few dishwasher images if you want one with closed door i may need to sort one out

```html
<!DOCTYPE html>
<html lang="en">
<head>
<meta charset="utf-8">
<title>Imprasio – Dare to Compare</title>
<link rel="stylesheet" href="https://fonts.googleapis.com/css2?family=Bangers&family=Roboto+Condensed:wght@400;800&display=swap">
<style>
  :root {
    --brand-green: #1fa84a;
    --sticker-yellow: #ffeb1a;
    --ink: #000000;
    --paper: #ffffff;
    --border-tone: #6e6e6e;
    --steel-light: #c9cbc9;
    --steel-dark: #7d807d;
    --washer-white: #e9ecef;
  }
  * { margin: 0; padding: 0; box-sizing: border-box; }
  html, body { width: 1200px; height: 2164px; overflow: hidden; background: var(--paper); }
  .billboard {
    position: relative; width: 1200px; height: 2164px; background: var(--paper);
    font-family: "Roboto Condensed", sans-serif;
  }
  .frame {
    position: absolute; left: 33px; top: 20px; width: 1134px; height: 2115px;
    border: 4px solid var(--ink); background: var(--paper);
  }
  .side-strip {
    position: absolute; top: 20px; width: 56px; height: 2115px;
    background: var(--border-tone);
    border: 4px solid var(--ink);
  }
  .side-strip.left { left: 33px; }
  .side-strip.right { left: 1111px; }
  .brand-bar {
    position: absolute; left: 89px; top: 24px; width: 1022px; height: 174px;
    display: flex; align-items: center; justify-content: center;
  }
  .brand-name {
    font-family: "Roboto Condensed", sans-serif; font-weight: 800;
    font-size: 132px; line-height: 1; color: var(--ink); letter-spacing: 1px;
  }
  .promo-field {
    position: absolute; left: 89px; top: 198px; width: 1022px; height: 1643px;
    background: var(--brand-green); overflow: hidden;
  }
  .sticker-text {
    position: absolute; font-family: "Bangers", sans-serif; color: var(--sticker-yellow);
    -webkit-text-stroke: 5px var(--ink); paint-order: stroke fill;
    text-shadow: 4px 5px 0 var(--ink); white-space: nowrap; line-height: 1;
  }
  .headline-price { left: 0; width: 100%; text-align: center; top: 60px; font-size: 96px; transform: rotate(-2deg); }
  .headline-warranty { left: 0; width: 100%; text-align: center; top: 178px; font-size: 96px; transform: rotate(-2deg); }
  .product { position: absolute; }
  .product-fridge {
    left: 345px; top: 315px; width: 423px; height: 797px;
    background: linear-gradient(90deg, var(--steel-dark), var(--steel-light) 30%, #e3e4e2 50%, var(--steel-light) 70%, var(--steel-dark));
  }
  .product-dishwasher {
    left: 43px; top: 755px; width: 560px; height: 439px;
    background: linear-gradient(160deg, #9a9c9a, #5f625f 60%, #3f423f);
  }
  .product-washer {
    left: 585px; top: 672px; width: 400px; height: 522px;
    background: linear-gradient(180deg, #f6f7f8, var(--washer-white) 45%, #b9bdc2);
    border-radius: 24px 24px 6px 6px;
  }
  .price-badge {
    position: absolute; width: 240px; height: 240px; border-radius: 50%;
    background: var(--ink); border: 6px solid var(--paper);
  }
  .price-badge .sticker-text {
    font-size: 118px; left: 50%; top: 50%; transform: translate(-50%, -50%) rotate(-12deg);
    -webkit-text-stroke: 0;
  }
  .price-badge .currency { font-size: 90px; }
  .badge-fridge { left: 640px; top: 396px; }
  .badge-dishwasher { left: 70px; top: 810px; }
  .badge-washer { left: 690px; top: 1000px; }
  .tagline-dare { left: 90px; top: 1230px; font-size: 230px; transform: rotate(-7deg); }
  .tagline-compare { left: 460px; top: 1440px; font-size: 128px; transform: rotate(-7deg); }
  .store-info {
    position: absolute; left: 89px; top: 1841px; width: 1022px; height: 290px;
    display: flex; flex-direction: column; justify-content: center; align-items: center;
    color: var(--ink); font-size: 47px; line-height: 67px; text-align: center;
  }
  .store-info .sep { padding: 0 12px; }
</style>
</head>
<body>
<div class="billboard">
  <div class="frame"></div>
  <div class="side-strip left" role="img" aria-label="Black and white chequered border strip"></div>
  <div class="side-strip right" role="img" aria-label="Black and white chequered border strip"></div>

  <header class="brand-bar">
    <span class="brand-name">Imprasio</span>
  </header>

  <main class="promo-field">
    <div class="sticker-text headline-price">OUR PRICES WON'T BE BEATEN</div>
    <div class="sticker-text headline-warranty">+ 5 YEAR WARRANTY</div>

    <div class="product product-fridge" role="img" aria-label="Stainless steel side by side fridge freezer"></div>
    <div class="product product-dishwasher" role="img" aria-label="Stainless steel dishwasher with door open and racks pulled out"></div>
    <div class="product product-washer" role="img" aria-label="White 8 kg top loader clothes washer"></div>

    <div class="price-badge badge-fridge"><span class="sticker-text"><span class="currency">$</span>1299</span></div>
    <div class="price-badge badge-dishwasher"><span class="sticker-text"><span class="currency">$</span>499</span></div>
    <div class="price-badge badge-washer"><span class="sticker-text"><span class="currency">$</span>699</span></div>

    <div class="sticker-text tagline-dare">DARE TO</div>
    <div class="sticker-text tagline-compare">COMPARE</div>
  </main>

  <footer class="store-info">
    <p>CNR MAROA &amp; KEREN ROAD<span class="sep">I</span>HALSTEAD</p>
    <p>PH: (09) 555 0142<span class="sep">I</span>W: imprasio.co.nz</p>
    <p>Ample parking<span class="sep">I</span>Debit<span class="sep">I</span>Credit<span class="sep">I</span>Store Card<span class="sep">I</span>Layby</p>
    <p>OPEN 7 DAYS 9am-5pm</p>
  </footer>
</div>
</body>
</html>
```